QT Lending - Tailored Lending and Mortgage Solutions

Hi,

We need a brochure for a new mortgage broking company based in Sydney New South Wales. We act as mortgage brokers to assist clients find the most suitable loans. More details as follows:

1. We offer the following services:
• Mortgage solutions tailored to your needs
• Asset Finance solutions
• Commercial/business lending solutions
• We can conduct over the phone interviews to save you time
• We have access to a wide panel of lenders to save you time and do all the
legwork for you to save you time and money. We also do not charge a brokerage fee.
• We do not charge you a fee on top of standard bank fees and charges for using our services

Important to have 'Call us now for a borrowing capacity or email us your details and we will call within 24 hours'.

We need the colors to suit our logo in the attachment. Please also include our contact numbers, ABN 48392017456 and photograph. Please contact me should you have any questions.

Many thanks,
Lulu

Target Market(s)

Nationwide

Industry/Entity Type

Finance

Font styles to use
Serif

Requirements
Must have
• - My photograph and contact details.
• - Pictures relating to the topic
• - Business name and logo as per attachment
• - folds into front, middle and back page.
• - double sided layout
• 1. We offer the following services:
• • Mortgage solutions tailored to your needs
• • Asset Finance solutions
• • Commercial/business lending solutions
• • We can conduct over the phone interviews to save you time
• • We have access to a wide panel of lenders to save you time and do all the
• legwork for you to save you time and money. We also do not charge a brokerage fee.
• • We do not charge you a fee on top of standard bank fees and charges for using our services
• Important to have 'Call us now for a borrowing capacity or email us your details and we will call within 24 hours'.

```html
<!DOCTYPE html>
<html lang="en">
<head>
<meta charset="utf-8">
<title>QT Lending Brochure</title>
<link rel="stylesheet" href="https://fonts.googleapis.com/css2?family=Bebas+Neue&family=Montserrat:ital,wght@0,400;0,500;0,600;0,700;1,600&display=swap">
<style>
:root{
  --ink:#1b1f21;
  --slate:#2b3234;
  --orange:#f0a020;
  --orange-deep:#d88a12;
  --grey-text:#a9abab;
  --body:#3a3a3a;
  --white:#ffffff;
  --bg:#000000;
}
*{margin:0;padding:0;box-sizing:border-box}
html,body{width:826px;height:1200px;overflow:hidden;background:var(--bg)}
body{position:relative;font-family:"Montserrat",sans-serif;color:var(--body)}
.abs{position:absolute}
.display{font-family:"Bebas Neue",sans-serif;letter-spacing:.3px}

.sheet{position:absolute;left:73px;width:680px;background:var(--white);overflow:hidden}
.sheet--outer{top:33px;height:525px}
.sheet--inner{top:618px;height:526px}

/* profile column */
.profile-band{left:0;top:0;width:226px;height:122px;background:var(--slate)}
.profile-photo{left:9px;top:14px;width:143px;height:189px;background:var(--white);padding:6px;box-shadow:0 1px 3px rgba(0,0,0,.25)}
.profile-photo div{width:100%;height:100%;background:linear-gradient(160deg,#8a5a3a,#c99a7c 55%,#e9e4df)}
.profile-name{left:17px;top:210px;font-size:10.5px;font-weight:700;color:var(--ink)}
.profile-role{left:17px;top:225px;font-size:10px;color:var(--ink)}
.profile-about{left:17px;top:248px;width:194px;font-size:9.2px;line-height:14.2px;color:var(--ink)}
.profile-cta{left:17px;top:378px;width:205px;font-size:10.3px;line-height:16px;color:var(--ink)}
.profile-cta .big{font-size:20px;font-weight:700;color:var(--orange);letter-spacing:.5px}
.profile-cta .mail{font-weight:600;font-style:italic}

/* cover header */
.cover-header{left:226px;top:0;width:454px;height:120px;background:var(--white)}
.service-list{left:13px;top:24px;font-size:27px;line-height:27px;color:var(--grey-text)}
.brand{left:252px;top:40px;text-align:left}
.brand-name{font-size:24px;font-weight:500;color:var(--slate);letter-spacing:.3px;display:flex;align-items:center;gap:6px}
.brand-name .dot{width:12px;height:12px;background:var(--orange)}
.brand-tag{font-size:6.5px;font-weight:600;color:var(--slate);letter-spacing:.2px;margin-top:2px}

/* cover panel */
.cover-panel{left:226px;top:120px;width:454px;height:405px;background:var(--orange)}
.cover-photo{left:0;top:0;width:454px;height:405px;background:linear-gradient(120deg,#e59a1c 0%,#f0a728 40%,#c98516 70%,#f2a822 100%)}
.contact-list{left:20px;top:252px;font-size:9.6px;color:var(--white);font-weight:500;list-style:none}
.contact-list li{display:flex;align-items:flex-start;gap:7px;margin-bottom:10px;line-height:11px}
.contact-list svg{flex:none;margin-top:1px}
.headline{left:244px;top:197px;font-size:35px;line-height:33px;color:var(--white)}
.abn{left:304px;top:386px;font-size:8px;color:#fbe7c2}

/* inner spread */
.tile{position:absolute;overflow:hidden}
.tile-photo-house{left:0;top:0;width:226px;height:213px;background:linear-gradient(150deg,#c9ccd0,#eef0f2 55%,#b9bec4)}
.tile-commercial{left:226px;top:0;width:226px;height:213px;background:var(--orange)}
.tile-photo-car{left:452px;top:0;width:228px;height:213px;background:linear-gradient(135deg,#e6e8ea,#8a9298 50%,#2a2f33)}
.divider{left:0;top:213px;width:680px;height:4px;background:var(--slate)}
.tile-home{left:0;top:217px;width:226px;height:219px;background:var(--white)}
.tile-photo-tower{left:226px;top:217px;width:226px;height:219px;background:linear-gradient(200deg,#bcd9ef,#4d86b8 55%,#1c3c5a)}
.tile-asset{left:452px;top:217px;width:228px;height:219px;background:var(--white)}

.service-head{position:absolute;display:flex;align-items:center;gap:7px;font-size:16.5px;font-weight:500}
.icon-box{width:25px;height:26px;background:var(--orange);display:flex;align-items:center;justify-content:center}
.icon-box--wide{width:37px}
.service-copy{position:absolute;font-size:9.8px;line-height:14.5px}

.tile-commercial .service-head{left:15px;top:44px;color:var(--white)}
.tile-commercial .icon-box{background:var(--white)}
.tile-commercial .service-copy{left:16px;top:84px;width:202px;color:var(--white)}
.tile-home .service-head{left:13px;top:50px;color:var(--ink)}
.tile-home .service-copy{left:14px;top:86px;width:190px;line-height:16px;color:var(--ink)}
.tile-asset .service-head{left:19px;top:55px;color:var(--ink)}
.tile-asset .service-copy{left:20px;top:91px;width:186px;color:var(--ink)}

.footer{left:0;top:436px;width:680px;height:90px;background:var(--slate);color:var(--white)}
.footer-address{left:0;top:15px;width:680px;text-align:center;font-size:10.5px;font-weight:600}
.footer-contacts{left:0;top:39px;width:680px;display:flex;justify-content:center;gap:36px;font-size:10.5px;font-weight:600}
.footer-contacts span{display:flex;align-items:center;gap:3px}
.disclaimer{left:0;top:71px;width:680px;text-align:center;font-size:7px}
</style>
</head>
<body>

<section class="sheet sheet--outer">
  <div class="abs profile-band"></div>
  <div class="abs profile-photo"><div role="img" aria-label="Portrait photograph of Lulu Marsh, director"></div></div>
  <div class="abs profile-name">Lulu Marsh</div>
  <div class="abs profile-role">QT Lending Director</div>
  <p class="abs profile-about">We are finance brokers based in Sydney New South Wales. Our aim is to help you find the most suitable lending solutions based on your individual needs. We also have access to a wide panel of lenders including the big 4 banks to save you all the legwork.</p>
  <p class="abs profile-cta">Contact us now for an appointment<br>on <span class="big">0400 555 123</span><br>or email us your enquiry at<br><svg width="10" height="7" viewBox="0 0 10 7"><rect width="10" height="7" fill="#1b1f21"/><path d="M0 0l5 4 5-4" stroke="#fff" fill="none"/></svg> <span class="mail">enquiries@qtlending.com.au</span><br>and we will contact you<br>within 24 hours</p>

  <div class="abs cover-header">
    <div class="abs service-list display">Home Loans<br>Commercial Loans<br>Asset Finance</div>
    <div class="abs brand">
      <div class="brand-name"><span class="dot"></span>QT LENDING</div>
      <div class="brand-tag">TAILORED LENDING &amp; MORTGAGE SOLUTIONS</div>
    </div>
  </div>

  <div class="abs cover-panel">
    <div class="abs cover-photo" role="img" aria-label="Orange-toned photograph of two business people shaking hands in an office"></div>
    <ul class="abs contact-list">
      <li><svg width="9" height="11" viewBox="0 0 9 11"><path d="M4.5 0a4 4 0 0 0-4 4c0 3 4 7 4 7s4-4 4-7a4 4 0 0 0-4-4z" fill="#fff"/><circle cx="4.5" cy="4" r="1.5" fill="#f0a020"/></svg>Level 3, 18 Harbour Street<br>Ryde NSW 2112</li>
      <li><svg width="9" height="9" viewBox="0 0 9 9"><path d="M1 3c0-2 7-2 7 0v1H6V3H3v1H1z" fill="#fff"/><rect x="1.5" y="5" width="6" height="3.5" fill="#fff"/></svg>02 9000 4821</li>
      <li><svg width="9" height="10" viewBox="0 0 9 10"><rect x="2" y="0.5" width="5" height="9" rx="1" fill="none" stroke="#fff"/></svg>0400 555 123</li>
      <li><svg width="9" height="7" viewBox="0 0 9 7"><rect width="9" height="7" fill="#fff"/><path d="M0 0l4.5 4L9 0" stroke="#f0a020" fill="none"/></svg>lulu@qtlending.com.au</li>
      <li><svg width="9" height="9" viewBox="0 0 9 9"><circle cx="4.5" cy="4.5" r="4" fill="none" stroke="#fff"/><path d="M.5 4.5h8M4.5.5c-2 2-2 6 0 8M4.5.5c2 2 2 6 0 8" stroke="#fff" fill="none" stroke-width=".8"/></svg>www.qtlending.com.au</li>
    </ul>
    <div class="abs headline display">Mortgage<br>Brokers<br>to assist clients<br>find the most<br>suitable loans</div>
    <div class="abs abn">ABN 48392017456</div>
  </div>
</section>

<section class="sheet sheet--inner">
  <div class="tile tile-photo-house" role="img" aria-label="Photograph of a small model house on a desk with people reviewing paperwork"></div>
  <div class="tile tile-commercial">
    <div class="service-head"><span class="icon-box"><svg width="15" height="15" viewBox="0 0 15 15"><rect x="1" y="5" width="5" height="10" fill="#f0a020"/><rect x="7" y="1" width="7" height="14" fill="#f0a020"/></svg></span>Commercial loans</div>
    <p class="service-copy">Lending solutions for clients looking to purchase non-residential properties that are income generating on a commercial scale. For example, shop fronts, warehouses and offices.</p>
  </div>
  <div class="tile tile-photo-car" role="img" aria-label="Photograph of a hand opening the door of a new car"></div>
  <div class="abs divider"></div>
  <div class="tile tile-home">
    <div class="service-head"><span class="icon-box"><svg width="15" height="14" viewBox="0 0 15 14"><path d="M7.5 1L1 7h2v6h3.5V9h2v4H12V7h2z" fill="#fff"/></svg></span>Home loans</div>
    <p class="service-copy">We will assist you find the most suitable loan to fund your residential /investment property purchase or if you are looking to refinance your existing loan.</p>
  </div>
  <div class="tile tile-photo-tower" role="img" aria-label="Photograph looking up at glass office towers against a blue sky"></div>
  <div class="tile tile-asset">
    <div class="service-head"><span class="icon-box icon-box--wide"><svg width="26" height="13" viewBox="0 0 30 14"><path d="M3 9l3-5h14l5 5h2v3H3z" fill="#fff"/><circle cx="9" cy="12" r="2" fill="#f0a020"/><circle cx="21" cy="12" r="2" fill="#f0a020"/></svg></span>Asset Finance</div>
    <p class="service-copy">For clients who are seeking finance to purchase cars or equipment for business use.</p>
  </div>

  <div class="abs footer">
    <div class="abs footer-address"><span style="color:var(--orange)">&#9679;</span> Level 3, 18 Harbour Street Ryde NSW 2112</div>
    <div class="abs footer-contacts">
      <span><svg width="10" height="9" viewBox="0 0 9 9"><path d="M1 3c0-2 7-2 7 0v1H6V3H3v1H1z" fill="#f0a020"/><rect x="1.5" y="5" width="6" height="3.5" fill="#f0a020"/></svg>02 9000 4821</span>
      <span><svg width="8" height="10" viewBox="0 0 9 10"><rect x="2" y="0.5" width="5" height="9" rx="1" fill="none" stroke="#f0a020"/></svg>0400 555 123</span>
      <span><svg width="10" height="7" viewBox="0 0 9 7"><rect width="9" height="7" fill="#f0a020"/><path d="M0 0l4.5 4L9 0" stroke="#2b3234" fill="none"/></svg>lulu@qtlending.com.au</span>
      <span><svg width="10" height="10" viewBox="0 0 9 9"><circle cx="4.5" cy="4.5" r="4.5" fill="#f0a020"/></svg>www.qtlending.com.au</span>
    </div>
    <div class="abs disclaimer">disclaimer: Approval is subject to Lender's criteria</div>
  </div>
</section>

</body>
</html>
```